Stationary mockup / corporate identity stationary presentation

We have developed a business card, envelope, and so on. We want to use a stationary mock up for internal presentation using a mock up template. The idea behind the logo is OK, we do not want to change, but we want to look for some creativity, we have a business card, letter head stationary, complements card, evenloppe etc. For mock up example templates, please look at: https://plumvexa.com/free-brandingidentity-stationery-psd-mockups/ We include the logo as word document. There are two logo's similar but differnet colors and name. These represent two activities within the same group company. For both we want to have a presentation and be stationary mock up. What we need is a complete presentation of different corporate identity items as a business card, envelope, letterhead stationary, compliments cards, pen, muck, etc. etc. mock up or please check: https: // plumvexa. com / free-brandingidentity-stationery-psd-mockups / http://www.gordalune.com/index.php?site=forum_topic&topic=1 Please look at website: http://www.tomselvikora.com/marquet/ This is sister website. For VILMORE will be the same.

Industry/Entity Type

Architecture

Font styles to use
Sans Serif

Colors
33a6d7

Requirements
Must have
• Please look at website: http://www.tomselvikora.com/marquet/ This is sister website. For VILMORE will be the same. How if you want. We want to search for uniformity in website and stationary design. But are open for suggestions offcourse.
Nice to have

```html
<!DOCTYPE html>
<html lang="en">
<head>
<meta charset="utf-8">
<title>Vilmore – Stationery Set</title>
<link rel="stylesheet" href="https://fonts.googleapis.com/css2?family=Inter:wght@400;600;800&display=swap">
<style>
  :root{
    --bg:#1d1e20;
    --blue:#4f98ea;
    --blue-light:#6eaef2;
    --blue-deep:#3c82d9;
    --ink:#111418;
    --text:#6b6f75;
    --paper:#ffffff;
    --frame:#e9eaec;
    --band:#2a2b2e;
  }
  *{margin:0;padding:0;box-sizing:border-box}
  html,body{width:1200px;height:801px;overflow:hidden;background:var(--bg);font-family:"Inter",Arial,sans-serif}
  .canvas{position:relative;width:1200px;height:801px}

  .brand{color:var(--ink);font-weight:800;letter-spacing:.02em;white-space:nowrap}

  /* folder */
  .folder{position:absolute;left:120px;top:150px;width:360px;height:510px;
    background:linear-gradient(160deg,var(--blue-light),var(--blue-deep))}

  /* letterhead */
  .letterhead{position:absolute;left:170px;top:190px;width:360px;height:509px;background:var(--paper);overflow:hidden}
  .letterhead .head{display:flex;justify-content:space-between;align-items:flex-start;padding:30px 28px 0}
  .letterhead .brand{font-size:17px;line-height:1}
  .contact{border-left:1px solid #d4d6da;padding-left:8px;font-size:5.5px;line-height:1.7;color:var(--text);white-space:nowrap}
  .contact .addr{color:var(--blue);font-weight:600}
  .letterhead .body{padding:42px 28px 0;font-size:6.6px;line-height:1.65;color:var(--text);width:300px}
  .letterhead .body p{margin-bottom:11px}
  .letterhead .deco{position:absolute;right:-40px;bottom:-30px;width:150px;height:150px;border:22px solid var(--frame)}
  .letterhead .rule{position:absolute;left:0;right:0;bottom:0;height:4px;background:var(--blue)}

  /* notebook */
  .notebook{position:absolute;left:590px;top:50px;width:240px;height:330px;border-radius:4px 14px 14px 4px;
    background:linear-gradient(160deg,var(--blue-light),var(--blue-deep));overflow:hidden}
  .notebook .panel{position:absolute;left:40px;top:90px;width:150px;height:150px;background:rgba(255,255,255,.08)}
  .notebook .brand{position:absolute;left:40px;top:157px;width:150px;text-align:center;font-size:15px}
  .notebook .band{position:absolute;right:28px;top:0;bottom:0;width:8px;background:var(--band)}

  /* envelope */
  .envelope{position:absolute;left:860px;top:70px;width:310px;height:160px;background:var(--paper);overflow:hidden}
  .envelope .brand{position:absolute;left:18px;top:20px;font-size:12px}
  .envelope .addr{position:absolute;left:18px;top:40px;font-size:6px;color:var(--blue);font-weight:600}
  .envelope .deco{position:absolute;right:20px;top:22px;width:70px;height:70px;border:12px solid var(--frame)}
  .envelope .rule{position:absolute;left:0;right:0;bottom:0;height:3px;background:var(--blue)}

  /* business cards */
  .card{position:absolute;width:250px;height:142px;overflow:hidden}
  .card-front{left:890px;top:275px;background:linear-gradient(160deg,var(--blue-light),var(--blue-deep));display:flex;align-items:center;justify-content:center}
  .card-front .brand{font-size:15px}
  .card-back{left:890px;top:450px;background:var(--paper);padding:20px}
  .card-back .brand{font-size:12px}
  .card-back .row{display:flex;justify-content:space-between;margin-top:34px}
  .card-back .name{color:var(--blue);font-size:8px;font-weight:600}
  .card-back .role{color:var(--text);font-size:5.5px;margin-top:2px}
  .card-back .contact{font-size:5px}
  .card-back .rule{position:absolute;left:0;right:0;bottom:0;height:3px;background:var(--blue)}
</style>
</head>
<body>
<main class="canvas">

  <div class="folder"></div>

  <article class="letterhead">
    <header class="head">
      <div class="brand">VILMORE</div>
      <div class="contact">
        <div class="addr">Level 00, 00 Example Street, Example, 000</div>
        <div>0000 000 000 &nbsp;|&nbsp; 0000 000 000</div>
        <div>contact@vilmore-studio.com</div>
        <div>www.vilmore-studio.com</div>
      </div>
    </header>
    <section class="body">
      <p>Vilmore designs calm, lasting buildings for people who live and work in them. Each project starts with the site, the light and the way a space will be used over many years.</p>
      <p>Our studio works across homes, offices and public places. We draw by hand, test in models and refine every detail with the client until the plan feels simple and clear.</p>
      <p>We believe good architecture is quiet. It frames daily life, uses honest materials and respects its neighbours. Thank you for your interest; we look forward to working with you.</p>
    </section>
    <div class="deco"></div>
    <div class="rule"></div>
  </article>

  <div class="notebook">
    <div class="panel"></div>
    <div class="brand">VILMORE</div>
    <div class="band"></div>
  </div>

  <div class="envelope">
    <div class="brand">VILMORE</div>
    <div class="addr">Level 00, 00 Example Street, Example, 2000</div>
    <div class="deco"></div>
    <div class="rule"></div>
  </div>

  <div class="card card-front">
    <div class="brand">VILMORE</div>
  </div>

  <div class="card card-back">
    <div class="brand">VILMORE</div>
    <div class="row">
      <div>
        <div class="name">Example Name</div>
        <div class="role">Lead Architect</div>
      </div>
      <div class="contact">
        <div class="addr">Level 00, 00 Example Street, Example, 000</div>
        <div>0000 000 000 &nbsp;|&nbsp; 0000 000 000</div>
        <div>contact@vilmore-studio.com</div>
        <div>www.vilmore-studio.com</div>
      </div>
    </div>
    <div class="rule"></div>
  </div>

</main>
</body>
</html>
```